Poster Design Project- kids dancing/sport

I need a poster design for a childrens dance and sport program!!
I have attached a brochure and logo designs. From the brochure please include information from sections titled "twirl'n'hop" and "themes". Also please put on the phone number and email address (found on the brochure). Emphasis on FUN!! Make poster colourful, very kid friendly and eye catching.
Some other things i would like on the poster are:
"Does your child love to dance, sing and play sport?? Why not enrol them in our fun-filled program?"
"From only $10.00 per class"
"Sign up for your FREE trial class today"
"A fun introduction to the joy of Dance, Sport and Music for 2-6yr olds. Held in your childcare centre!!"
Hi!!
I would like to stress its TRIAL class not TRAIL class. Please feel free to play around with the information, it doesnt need to be in one blurb. Also i have updated the brief. I would like "Does you child love to dance, sing or play sport? Why not enrol in our fun filled program?" or something to that effect!!
Thanks!!!!
2-6yr olds and their parents
Childcare

```html
<!DOCTYPE html>
<html lang="en">
<head>
<meta charset="utf-8">
<title>Twirl 'n' Hop Poster</title>
<link href="https://fonts.googleapis.com/css2?family=Short+Stack&display=swap" rel="stylesheet">
<style>
  :root {
    --sky: #1a9ad8;
    --grape: #7a1d98;
    --lime: #c6d82a;
    --berry: #e04356;
    --butter: #f8d878;
    --leaf: #86c262;
    --aqua: #5bbde4;
    --plum: #64479a;
    --ink: #3a3335;
    --white: #ffffff;
    --red: #e33a3e;
    --blue-text: #1d6db4;
    --magenta: #d8236f;
    --yellow: #fff23a;
    --night: #202020;
    --orange: #f2a03a;
    --font: "Short Stack", "Comic Sans MS", cursive;
  }
  * { box-sizing: border-box; margin: 0; padding: 0; }
  html, body { width: 849px; height: 1200px; overflow: hidden; }
  body { font-family: var(--font); background: var(--white); }
  .poster { position: relative; width: 849px; height: 1200px; overflow: hidden; }

  .band { position: absolute; left: 0; width: 849px; }
  .band--sky { top: 0; height: 132px; background: var(--sky); }
  .band--grape { top: 132px; height: 118px; background: var(--grape); }
  .band--lime { top: 250px; height: 181px; background: var(--lime); }

  .stripe { position: absolute; top: 431px; height: 735px; }
  .stripe--berry { left: 0; width: 158px; background: var(--berry); }
  .stripe--butter { left: 158px; width: 179px; background: var(--butter); }
  .stripe--leaf { left: 337px; width: 178px; background: var(--leaf); }
  .stripe--aqua { left: 515px; width: 175px; background: var(--aqua); }
  .stripe--plum { left: 690px; width: 159px; background: var(--plum); }

  .footer-bar { position: absolute; left: 0; top: 1166px; width: 849px; height: 34px; background: var(--night); }
  .footer-bar__text { position: absolute; right: 18px; top: 7px; color: var(--red); font-size: 16px; white-space: nowrap; }

  .dot { position: absolute; border-radius: 50%; }

  .art { position: absolute; }
  .art--dancer { left: 600px; top: 20px; width: 249px; height: 340px;
    background: linear-gradient(160deg, #3d6fb8 0%, #b5542a 50%, #5a4236 100%); opacity: .85;
    border-radius: 60px 0 0 120px; }
  .art--ball { left: 0; top: 282px; width: 56px; height: 108px; border-radius: 0 54px 54px 0;
    background: linear-gradient(135deg, #f4f4f4, #8a8a8a); }
  .art--bowling { left: 735px; top: 535px; width: 110px; height: 100px; border-radius: 40px;
    background: linear-gradient(160deg, #b7d35a, #3f63a5); }
  .art--kids { left: 0; top: 930px; width: 849px; height: 236px;
    background: linear-gradient(180deg, rgba(34,34,34,0) 0%, rgba(34,34,34,.9) 30%, #232323 100%); }

  .brand { position: absolute; left: 30px; top: 150px; color: var(--white); font-family: var(--font);
    font-weight: 400; font-size: 72px; line-height: 1; white-space: nowrap; }

  .tagline { position: absolute; color: var(--ink); white-space: nowrap; line-height: 1; }
  .tagline--every { left: 42px; top: 440px; font-size: 40px; }
  .tagline--magic { left: 170px; top: 398px; font-size: 33px; transform: rotate(-6deg); transform-origin: left center; }
  .tagline--price { left: 395px; top: 448px; font-size: 31px; transform: rotate(4deg); transform-origin: left center; }

  .cta { position: absolute; left: 205px; top: 492px; color: var(--red); font-size: 27px; line-height: 1.15; transform: rotate(5deg); transform-origin: left top; white-space: nowrap; }

  .copy { position: absolute; font-size: 14px; line-height: 1.9; }
  .copy--ask { left: 40px; top: 545px; width: 116px; color: var(--white); }
  .copy--about { left: 170px; top: 612px; width: 162px; color: var(--blue-text); }
  .copy--skills { left: 355px; top: 708px; width: 156px; color: var(--magenta); }

  .themes-title { position: absolute; left: 665px; top: 628px; color: var(--yellow); font-size: 28px; transform: rotate(12deg); }
  .themes { position: absolute; left: 536px; top: 555px; list-style: none; color: var(--white); font-size: 13.5px; line-height: 27.4px; white-space: nowrap; letter-spacing: -0.2px; }
  .themes li::before { content: "•"; margin-right: 9px; }

  .contact { position: absolute; left: 42px; color: var(--white); white-space: nowrap; line-height: 1; }
  .contact--phone { top: 1042px; font-size: 50px; letter-spacing: 2px; }
  .contact--email { top: 1132px; font-size: 27px; }
</style>
</head>
<body>
<main class="poster">
  <div class="band band--sky"></div>
  <div class="band band--grape"></div>
  <div class="band band--lime"></div>

  <div class="stripe stripe--berry"></div>
  <div class="stripe stripe--butter"></div>
  <div class="stripe stripe--leaf"></div>
  <div class="stripe stripe--aqua"></div>
  <div class="stripe stripe--plum"></div>

  <span class="dot" style="left:118px;top:285px;width:42px;height:42px;background:#8fd4f0"></span>
  <span class="dot" style="left:35px;top:325px;width:70px;height:70px;background:var(--orange)"></span>
  <span class="dot" style="left:125px;top:345px;width:30px;height:30px;background:#9cbc3a"></span>
  <span class="dot" style="left:270px;top:878px;width:70px;height:70px;background:var(--orange)"></span>
  <span class="dot" style="left:222px;top:907px;width:28px;height:28px;background:#9cbc3a"></span>
  <span class="dot" style="left:130px;top:915px;width:16px;height:16px;background:#c8d88a"></span>

  <div class="art art--dancer" role="img" aria-label="Illustration of a girl doing a handstand on a skateboard"></div>
  <div class="art art--ball" role="img" aria-label="Soccer ball"></div>
  <div class="art art--bowling" role="img" aria-label="Bowling ball and pins"></div>
  <div class="art art--kids" role="img" aria-label="Row of children's silhouettes dancing"></div>

  <h1 class="brand">Twirl 'n' Hop</h1>

  <p class="tagline tagline--every">Every</p>
  <p class="tagline tagline--magic">class is a magical place to be ...</p>
  <p class="tagline tagline--price">From only $10 per class</p>

  <p class="cta">sign up for a FREE<br>trial class today</p>

  <p class="copy copy--ask">Does your child love to dance, sing or play sport ... why not enrol in our Fun Filled program?</p>
  <p class="copy copy--about">Twirl 'n' Hop offers little boys and girls a range of FUN classes, held in your childcare centre, that will introduce them to the wonderful world of music, movement and P.E.</p>
  <p class="copy copy--skills">Children will develop a range of skills including balance, co-ordination, confidence, motor skills, creativity, rhythm and much more!</p>

  <p class="themes-title">THEMES</p>
  <ul class="themes">
    <li>Jumping Jellybeans</li>
    <li>Under the Sea</li>
    <li>Superheros</li>
    <li>Jungle Jam</li>
    <li>Movie Magic</li>
    <li>Balancing Bugs</li>
    <li>Gymnastics &amp; Rhythmic Gymnastics</li>
    <li>Disco Divas &amp; Singing Superstars</li>
    <li>Hawaiian Holiday</li>
    <li>Circus</li>
    <li>Space</li>
    <li>Bowling &amp; Ball Skills</li>
    <li>Colours &amp; Shapes</li>
    <li>Monsters</li>
    <li>Magical Fairytales</li>
    <li>Sport and Cheerleading</li>
    <li>Mexican Fiesta</li>
    <li>Animals</li>
    <li>Aboriginal Adventure</li>
    <li>Its Party Time</li>
  </ul>

  <p class="contact contact--phone">P: 0400 555 019</p>
  <p class="contact contact--email">E: twirlnhop@kidsmail.com</p>

  <footer class="footer-bar">
    <p class="footer-bar__text">Twirl 'n' Hop also offers birthday parties!!!</p>
  </footer>
</main>
</body>
</html>
```